Mock up Blog Design for midwife that works in a hospital setting

We are looking to have a design created for a midwife. This blog will be used to share information or experiences related to pregnancy, child birth and motherhood with its readership. It should convey a feeling of warmth and security to women who are looking for a partner in the birthing processes.

We are asking you to design the layout, not code it up. This is a concept project only.

NOtes from the midwife

​So I'm just going to put in links to a few blogs and say what I like and don't like about each one:

rosalindpeverell.com.au/blog/

I like how there is a colorful background that has to do with her books; maybe mine could have a background with baby stuff in the background. It's also nice how there's an index of recent postings with the subject listed and how the postings are sorted by date, all on the same page.

www.steadybottlebrigade.com

I like that this one is set up like a website with tabs for resources, a bio, reader comments, etc.

cradlecorner.tendrilfoundation.org

This blog has a very calming color scheme, which is welcoming. I like that there's a picture for every posting, and that at the bottom of the posting there is a little glossary with the subjects that are covered in the posting. Also, I like the way that the date of each blog is done.

bellyhumourhub.blogspot.com

This one is really funny, and similar in intention to the one that I want to do. I like that she has a glossary of medical terms so that readers can look them up.

General comments:
I'm not sure how much DKWH wants their logo on my blog or in the blog name...
I would like to be able to vet comments before they appear on the blog, so that if there's an inappropriate one, I can screen it out.
I would also like to be able to see how many people have viewed the site.
Updates

Target Market(s)

Pregnant mothers, new moms, hopeful moms

Industry/Entity Type

Hospital

Requirements
Must have
• Incorporation of the logo and at least one of the photographs that will be provided In the header
Should not have
• Should not look canned, rigid or boxy.

```html
<!DOCTYPE html>
<html lang="en">
<head>
<meta charset="utf-8">
<title>Dawnlight Midwifery — Blog</title>
<link href="https://fonts.googleapis.com/css2?family=Lobster&family=Lato:wght@400&family=Montserrat:wght@400&display=swap" rel="stylesheet">
<style>
  :root {
    --paper: #ece2d8;
    --paper-deep: #e2d4c6;
    --rose: #a84c78;
    --rose-dark: #8a3a60;
    --rose-soft: #c97aa0;
    --ink: #2b2622;
    --heading: #4a3d36;
    --dots: #c8ccd2;
    --panel: #ffffff;
    --sidebar: #d8d8d8;
    --link: #3d8fd6;
    --deco-a: #e8cfc8;
    --deco-b: #d9c2b4;
  }
  * { box-sizing: border-box; margin: 0; padding: 0; }
  html, body { width: 1200px; height: 1000px; overflow: hidden; }
  body {
    position: relative;
    background: radial-gradient(ellipse at 50% 40%, var(--paper) 0%, var(--paper-deep) 100%);
    font-family: "Lato", sans-serif;
    color: var(--ink);
  }
  .deco-side {
    position: absolute; top: 190px; width: 165px; height: 810px;
    background: linear-gradient(180deg, rgba(232,207,200,0.55) 0%, rgba(217,194,180,0.75) 60%, rgba(230,200,190,0.8) 100%);
  }
  .deco-left { left: 0; }
  .deco-right { right: 0; }
  .page {
    position: absolute; left: 165px; top: 120px; width: 870px; height: 880px;
    background: var(--panel);
    box-shadow: 0 0 10px rgba(0,0,0,0.12);
  }
  .lace {
    position: absolute; left: 165px; top: 84px; width: 870px; height: 40px;
    background: #f1ebe4; border-radius: 18px 18px 0 0;
  }
  .ribbon { position: absolute; left: 100px; top: 114px; }
  .nav {
    position: absolute; top: 147px; left: 0; width: 1200px;
    font-family: "Montserrat", sans-serif; font-size: 13px; color: #fff; letter-spacing: 0.2px;
  }
  .nav a { position: absolute; color: #fff; text-decoration: none; }
  .logo {
    position: absolute; left: 498px; top: 29px; width: 145px; height: 126px;
    background: #fff; border: 3px solid var(--rose);
    box-shadow: 0 2px 4px rgba(0,0,0,0.2);
    display: flex; flex-direction: column; align-items: center; justify-content: center;
    font-family: "Lato", sans-serif; color: var(--rose); text-align: center;
  }
  .logo-mark { width: 22px; height: 22px; border-radius: 50%; background: var(--rose); margin-bottom: 10px; }
  .logo-name { font-size: 20px; line-height: 1.1; }
  .logo-sub { font-size: 20px; line-height: 1.1; }
  .title {
    position: absolute; font-family: "Lobster", cursive; color: var(--heading); font-weight: 400;
  }
  .welcome-title { left: 203px; top: 208px; font-size: 35px; }
  .divider { position: absolute; left: 203px; width: 532px; border-top: 2px dotted var(--dots); }
  .divider-dot {
    position: absolute; left: 252px; top: -6px; width: 11px; height: 9px;
    background: #b8c0c8; border-radius: 50%;
  }
  .intro {
    position: absolute; left: 203px; top: 285px; width: 540px;
    font-size: 15px; line-height: 17.5px;
  }
  .photo {
    position: absolute; left: 292px; top: 372px; width: 444px; height: 372px;
    background: linear-gradient(160deg, #f6f5f3 0%, #efeae6 55%, #d9b7ae 100%);
  }
  .date-badge {
    position: absolute; left: 203px; top: 815px; width: 62px; height: 62px; border-radius: 50%;
    background: var(--rose); color: #fff; text-align: center;
    font-family: "Montserrat", sans-serif; font-size: 14px; line-height: 16px; padding-top: 15px;
  }
  .date-badge::after {
    content: ""; position: absolute; inset: 4px; border-radius: 50%;
    border: 1px dashed rgba(255,255,255,0.6);
  }
  .post-title { left: 291px; top: 800px; font-size: 22px; }
  .post-meta {
    position: absolute; left: 292px; top: 841px;
    font-family: "Montserrat", sans-serif; font-size: 12px; color: var(--rose); text-transform: uppercase;
  }
  .post-excerpt {
    position: absolute; left: 292px; top: 867px; width: 450px;
    font-size: 15px; line-height: 17.5px;
  }
  .post-excerpt a { color: var(--link); text-decoration: none; }
  .sidebar {
    position: absolute; left: 790px; top: 219px; width: 204px; height: 732px;
    background: var(--sidebar); border: 1px solid #cfcfcf;
  }
</style>
</head>
<body>
  <div class="deco-side deco-left" role="img" aria-label="Nursery illustration: hanging baby mobile with hearts and stars, a plush bunny and alphabet blocks"></div>
  <div class="deco-side deco-right" role="img" aria-label="Nursery illustration: hanging baby mobile with hearts and stars, a plush bunny and alphabet blocks"></div>

  <div class="page"></div>
  <div class="lace" role="img" aria-label="Scalloped lace trim"></div>

  <svg class="ribbon" width="1000" height="72" viewBox="0 0 1000 72">
    <polygon points="0,2 60,2 60,58 0,58 28,30" fill="var(--rose-dark)"/>
    <polygon points="1000,2 940,2 940,58 1000,58 972,30" fill="var(--rose-dark)"/>
    <rect x="56" y="8" width="888" height="62" fill="var(--rose)"/>
    <line x1="56" y1="15" x2="944" y2="15" stroke="#fff" stroke-opacity="0.6" stroke-dasharray="4 3"/>
    <line x1="56" y1="63" x2="944" y2="63" stroke="#fff" stroke-opacity="0.6" stroke-dasharray="4 3"/>
  </svg>

  <nav class="nav">
    <a style="left:201px" href="#">HOME</a>
    <a style="left:271px" href="#">CATEGORIES</a>
    <a style="left:380px" href="#">RESOURCES</a>
    <a style="left:678px" href="#">GALLERY</a>
    <a style="left:761px" href="#">GLOSSARY</a>
    <a style="left:851px" href="#">ABOUT ME</a>
    <a style="left:945px" href="#">CONTACT</a>
  </nav>

  <div class="logo">
    <div class="logo-mark"></div>
    <div class="logo-name">Dawnlight</div>
    <div class="logo-sub">Midwifery</div>
  </div>

  <h1 class="title welcome-title">Welcome</h1>
  <div class="divider" style="top:263px"><span class="divider-dot"></span></div>

  <p class="intro">Hello! Welcome to our first blog post on our newly revamped website!<br>
  Take a moment to explore our new site, perhaps bookmark us, and be sure to check back regularly for more information about our services as well as<br>useful news and tips.</p>

  <div class="photo" role="img" aria-label="Photo of a smiling mother with two young children playing doctor with a stethoscope and otoscope"></div>

  <div class="divider" style="top:777px"><span class="divider-dot"></span></div>

  <div class="date-badge">FEB<br>28</div>
  <h2 class="title post-title">The sleeping baby secret film club</h2>
  <p class="post-meta">Tags: Baby, Tips / Posted by: Author</p>
  <p class="post-excerpt">One of the big differences between your first and second babies is the amount of time you get to spend on the sofa, feeding, napping, and trapped under them when they sleep. As a baby Clara didn't want to be put down, I didn't want to put her down. Nothing got done for ages when we were at home, but that was OK. <a href="#">[...]</a></p>

  <div class="divider" style="top:981px"><span class="divider-dot"></span></div>

  <aside class="sidebar"></aside>
</body>
</html>
```